TIMBER DECK COMPANY FLYER

We need a flyer design for a Timber Decking company, we specialise in timber decks, stairs, privacy screens, maintenance and pergolas. I have attatched some pictures which you can incorporate if you think they need cropping go for it. We offer amazing decks at affordable prices by qualified tradespeople.
My logo is a dull green I would like this to be changed to a more lime bright green please. Also my logo is too big I would like this logo halved in size please. And the colours in the brochure maybe a blackbackground with lime green and other colours you think will work. We will also beat any reputable Decking companies quote by 10%. Our decks add style, class, longjevity and practicality to any home. The final design should be modern and cutting edge.

Target Market(s)

home owners

Industry/Entity Type

It Company

Logo Text

CRISP PLANKWORKS GROUP

Requirements
Must have
• DECKS
STAIRS
PERGOLAS
PRIVACY SCREENS
DECK MAINTENANCE

CONTACT-GORDON-0438261507

MUST HAVE LIKE US ON PAGEBOARD LOGO

www.crispplankworksgroup.com.au
Nice to have
• Please let me know if need more photos etc

```html
<!DOCTYPE html>
<html lang="en">
<head>
<meta charset="utf-8">
<title>Crisp Plankworks Group – Timber Decking Flyer</title>
<link rel="stylesheet" href="https://fonts.googleapis.com/css2?family=Roboto+Condensed:wght@400;700&display=swap">
<style>
  :root {
    --lime: #c6ef00;
    --ink: #0a0a0a;
    --white: #ffffff;
    --wood-dark: #9c6a4c;
    --wood-mid: #c89777;
    --wood-light: #dcb79c;
  }
  html, body {
    margin: 0;
    padding: 0;
    width: 1200px;
    height: 930px;
    overflow: hidden;
    background: var(--lime);
  }
  .flyer {
    position: relative;
    width: 1200px;
    height: 930px;
    overflow: hidden;
    background: var(--lime);
    font-family: "Roboto Condensed", "Arial Narrow", sans-serif;
    color: var(--ink);
  }
  .deck-backdrop {
    position: absolute;
    inset: 0 0 auto 0;
    height: 520px;
    background:
      linear-gradient(180deg, rgba(198,239,0,0) 0%, rgba(198,239,0,0) 38%, rgba(198,239,0,0.7) 62%, var(--lime) 88%),
      linear-gradient(100deg, var(--wood-mid) 0%, var(--wood-light) 35%, var(--wood-mid) 60%, var(--wood-dark) 100%);
  }
  .brand-square {
    position: absolute;
    left: 48px;
    top: 40px;
    width: 146px;
    height: 146px;
    background: var(--ink);
  }
  .brand-name {
    position: absolute;
    left: 348px;
    top: 26px;
    margin: 0;
    font-weight: 700;
    color: var(--ink);
    text-transform: uppercase;
    line-height: 1;
  }
  .brand-name .line-main {
    display: block;
    font-size: 98px;
    letter-spacing: -1px;
  }
  .brand-name .line-sub {
    display: block;
    font-size: 62px;
    letter-spacing: 62px;
    margin-top: 6px;
    font-weight: 400;
  }
  .services {
    position: absolute;
    left: 48px;
    top: 232px;
    margin: 0;
    padding: 0;
    list-style: none;
    font-weight: 700;
    font-size: 47px;
    line-height: 60px;
    color: var(--ink);
  }
  .contact {
    position: absolute;
    left: 48px;
    top: 540px;
    color: var(--white);
    font-weight: 700;
  }
  .contact-name {
    display: block;
    font-size: 40px;
    line-height: 44px;
  }
  .contact-phone {
    display: block;
    font-size: 60px;
    line-height: 60px;
  }
  .promo {
    position: absolute;
    right: 0;
    margin: 0;
    background: var(--ink);
    color: var(--lime);
    font-weight: 700;
    font-size: 27px;
    line-height: 38px;
    text-align: center;
    box-sizing: border-box;
    padding-top: 5px;
  }
  .promo-quote { top: 258px; left: 630px; height: 86px; }
  .promo-style { top: 367px; left: 632px; height: 86px; }
  .web {
    position: absolute;
    left: 633px;
    top: 502px;
    font-weight: 700;
    font-size: 28px;
    color: var(--ink);
  }
  .social-badge {
    position: absolute;
    left: 782px;
    top: 553px;
    width: 232px;
    height: 72px;
    background: var(--white);
    border-radius: 12px;
    display: flex;
    align-items: center;
    gap: 12px;
    padding: 0 14px;
    box-sizing: border-box;
  }
  .social-square {
    width: 44px;
    height: 44px;
    background: var(--ink);
    flex: none;
  }
  .social-text {
    font-weight: 700;
    font-size: 22px;
    line-height: 24px;
    color: var(--ink);
  }
  .gallery {
    position: absolute;
    top: 657px;
    left: 0;
    width: 1200px;
    height: 245px;
  }
  .gallery-tile {
    position: absolute;
    top: 0;
    height: 245px;
  }
  .tile-pool-deck {
    left: 0; width: 287px;
    background: linear-gradient(180deg, #8fa070 0%, #b0623e 40%, #7a2f1a 100%);
  }
  .tile-pool-boardwalk {
    left: 290px; width: 322px;
    background: linear-gradient(90deg, #4f7a3a 0%, #a4552f 35%, #3fb5d6 65%, #6c9c45 100%);
  }
  .tile-plunge-pool {
    left: 614px; width: 323px;
    background: linear-gradient(180deg, #5a5f5c 0%, #c7b194 30%, #1e3b3b 55%, #a8381c 100%);
  }
  .tile-stairs {
    left: 940px; width: 260px;
    background: linear-gradient(90deg, #3f6a2c 0%, #5e8a3c 40%, #d9c4a2 75%, #e7d6b8 100%);
  }
</style>
</head>
<body>
<main class="flyer">
  <div class="deck-backdrop" role="img" aria-label="Close-up photograph of freshly oiled hardwood deck boards"></div>

  <header class="brand">
    <div class="brand-square"></div>
    <h1 class="brand-name">
      <span class="line-main">CRISP PLANKWORKS</span>
      <span class="line-sub">GROUP</span>
    </h1>
  </header>

  <ul class="services">
    <li>DECKS</li>
    <li>STAIRS</li>
    <li>PERGOLAS</li>
    <li>PRIVACY SCREENS</li>
    <li>DECK MAINTENANCE</li>
  </ul>

  <div class="contact">
    <span class="contact-name">CONTACT GORDON</span>
    <span class="contact-phone">0438261507</span>
  </div>

  <p class="promo promo-quote">WE WILL&nbsp; BEAT ANY REPUTABLE DECKING<br>COMPANIES QUOTE&nbsp; BY 10%.</p>
  <p class="promo promo-style">OUR DECKS ADD STYLE, CLASS, LONGEVITY<br>AND PRACTICALITY TO ANY HOME.</p>

  <div class="web">www.crispplankworksgroup.com.au</div>

  <div class="social-badge">
    <span class="social-square"></span>
    <span class="social-text">Follow us on<br>PAGEBOARD</span>
  </div>

  <section class="gallery">
    <div class="gallery-tile tile-pool-deck" role="img" aria-label="Photo of a curved timber deck beside a backyard pool"></div>
    <div class="gallery-tile tile-pool-boardwalk" role="img" aria-label="Photo of a timber boardwalk alongside a pool with glass fencing"></div>
    <div class="gallery-tile tile-plunge-pool" role="img" aria-label="Photo of a plunge pool surrounded by red timber decking and sandstone"></div>
    <div class="gallery-tile tile-stairs" role="img" aria-label="Photo of new timber stairs with slatted privacy screen"></div>
  </section>
</main>
</body>
</html>
```